Engaging online lending company website

We already have a website at www.kelbrookfinance.com.au however it's nowhere near engaging enough. We are a fintech online brokerage company providing fantastic and super quick turnaround times on vehicle and mortgage loans. We need a website that is engaging with lots of call to actions and quote forms to capture details.

Target Market(s)

Young, technology savvy Australian's requiring finance. Aged between 20 - 45

Industry/Entity Type

Finance

Coding

Coded - Design and coding required

Requirements
Must have
• Get a Quick Quote Call to Action Box
• Get a Quick Quote (Express)
• Calculator Designs (2) – Home loan repayment and car loan repayment
• How it Works – Engaging design showing our 4 step loans process
• Banners: 1x for lending panel, 1 for current interest rates (similar to marlow lending home page), 1x Quill Gauge for customer reviews
• Banner on each page: Similar to Oakvale Finance “Today’s Best Rate” see below:
• Lots of well placed call to action buttons and quick quote forms on each page
• Apply Now page (similar fields to: https://www.marlowlendingsolutions.com.au/pre-approval/)

```html
<!DOCTYPE html>
<html lang="en">
<head>
<meta charset="utf-8">
<title>Kelbrook Lending Solutions</title>
<link href="https://fonts.googleapis.com/css2?family=Open+Sans:wght@400;600;700;800&family=Roboto+Condensed:wght@700&display=swap" rel="stylesheet">
<style>
:root{
  --blue:#1c9fd2;
  --navy:#113f5f;
  --navy-dark:#0b2f48;
  --orange:#fbb416;
  --ink:#1f3c52;
  --text:#555f66;
  --grey:#f1f2f3;
  --grey-mid:#e6e7e8;
  --line:#d6dadd;
  --white:#fff;
}
*{box-sizing:border-box;margin:0;padding:0}
a{text-decoration:none}
html,body{width:1200px;height:3636px;overflow:hidden}
body{font-family:"Open Sans",Arial,sans-serif;color:var(--text);background:var(--white);position:relative}
.section{position:absolute;left:0;width:1200px}
.btn{display:inline-flex;align-items:center;justify-content:center;font-weight:700;text-transform:uppercase;color:#fff;border:0}
h2.title{font-size:25px;font-weight:700;color:var(--navy);text-transform:uppercase;letter-spacing:.3px}

/* header */
.site-header{top:0;height:102px}
.brand{position:absolute;left:73px;top:30px;font-size:28px;font-weight:800;color:var(--navy);line-height:1.05;width:300px}
.brand small{display:block;font-size:14px;letter-spacing:3px}
.service{position:absolute;right:73px;top:22px;display:flex;align-items:center;gap:16px}
.service-text{text-align:right;color:var(--blue)}
.service-text span{display:block;font-size:14px;font-weight:600}
.service-text strong{display:block;font-size:31px;font-weight:700;line-height:1.05}
.main-nav{top:102px;left:73px;width:1054px;height:50px;background:var(--navy);display:flex;align-items:center;z-index:3}
.main-nav a{color:#fff;font-size:13px;font-weight:700;display:flex;align-items:center;gap:10px;padding:0 26px}
.main-nav a.cta{margin-left:auto;background:var(--blue);height:40px;margin-right:5px;padding:0 20px}

/* hero */
.hero{top:130px;height:544px}
.hero-photo{position:absolute;inset:0;background:linear-gradient(100deg,#2e3338 0%,#6d7379 38%,#a9b0b5 55%,#59606a 78%,#2b3036 100%)}
.hero-copy{position:absolute;left:73px;top:160px}
.hero-copy h1{font-family:"Roboto Condensed",Arial,sans-serif;color:#fff;font-size:45px;line-height:1.1;text-transform:uppercase}
.hero-copy .btn{margin-top:24px;background:var(--blue);font-size:14px;height:44px;padding:0 14px;border:2px solid #fff}
.quote-box{position:absolute;left:766px;top:88px;width:354px;height:407px;background:#fff;padding:22px 24px;text-align:center}
.quote-box h3{font-size:23px;color:var(--navy);font-weight:700}
.quote-box .hint{font-size:11px;margin-top:6px}
.loan-icons{display:flex;justify-content:center;gap:36px;margin:10px 0 14px}
.fields{display:grid;grid-template-columns:1fr 1fr;gap:14px 12px}
.fields .wide{grid-column:1/3}
.field{height:38px;border:1px solid var(--line);font-size:12px;text-align:left;padding:10px 12px;color:#888}
.business{display:flex;align-items:center;gap:8px;font-size:13px;color:var(--navy);font-weight:600;margin:14px 0 12px}
.radio{width:12px;height:12px;border:1px solid #999;border-radius:50%;display:inline-block}
.business label{font-weight:400;display:flex;align-items:center;gap:4px;color:var(--text)}
.quote-box .btn{width:100%;height:46px;background:var(--orange);font-size:17px}
.quote-box .terms{font-size:11px;margin-top:10px;line-height:1.45}

/* rates strip */
.rate-strip{top:674px;height:213px;background:linear-gradient(#fff,#f0f1f2)}
.best-rate{position:absolute;left:73px;top:58px;width:358px}
.best-rate .tag{height:49px;background:var(--orange);color:#fff;font-size:17px;font-weight:700;display:flex;align-items:center;justify-content:center}
.best-rate .date{display:flex;justify-content:center;align-items:center;gap:14px;margin-top:20px;color:var(--ink);font-size:20px;font-weight:600}
.rate-card{position:absolute;top:56px;width:306px;height:104px;background:#fff;border:1px solid var(--line);padding:10px 24px}
.rate-card span{font-size:16px;color:var(--blue);text-transform:uppercase}
.rate-card strong{display:block;font-size:50px;font-weight:400;color:var(--ink);line-height:1.1}
.rate-card strong sup{font-size:26px}
.rate-card em{position:absolute;right:12px;bottom:14px;font-style:normal;font-size:12px;color:var(--ink);font-weight:600;text-transform:uppercase}

/* interest / about */
.rates-about{top:887px;height:495px;background:var(--grey)}
.interest{position:absolute;left:73px;top:86px;width:490px}
.col-heads{position:absolute;left:228px;top:40px;display:flex;gap:28px;font-size:11px;text-align:center;color:var(--ink);line-height:1.1}
.rate-row{position:relative;display:flex;align-items:center;height:48px;margin-top:22px;background:#fff;margin-left:28px;padding-left:50px}
.rate-row.first{margin-top:56px}
.rate-row .icon{position:absolute;left:-28px;top:-4px;width:56px;height:56px;border-radius:50%;background:var(--blue);display:flex;align-items:center;justify-content:center}
.rate-row .name{width:150px;font-size:18px;color:var(--ink)}
.rate-row .num{width:90px;font-size:24px;color:var(--ink)}
.rate-row .btn{margin-left:auto;margin-right:10px;width:80px;height:34px;background:var(--orange);font-size:12px}
.divider{position:absolute;left:582px;top:80px;width:1px;height:350px;background:var(--line)}
.about{position:absolute;left:606px;top:86px;width:520px}
.about p{font-size:16px;line-height:1.65;margin-top:16px}
.calc-row{display:flex;gap:14px;margin-top:24px}
.calc-row .btn{flex:1;height:70px;justify-content:space-between;text-transform:none;font-size:17px;padding:0 16px;text-align:left;line-height:1.3}
.calc-row .home{background:var(--navy)}
.calc-row .car{background:var(--blue)}

/* how it works */
.how{top:1382px;height:405px;text-align:center}
.how h2{margin-top:48px}
.steps{position:absolute;left:73px;top:126px;width:1054px;display:flex;justify-content:space-between}
.step{width:218px;height:208px;background:var(--grey-mid);border-radius:6px;position:relative;padding-top:40px}
.step .circle{width:88px;height:88px;border-radius:50%;background:#fff;margin:0 auto;display:flex;align-items:center;justify-content:center}
.step .n{position:absolute;left:50px;top:28px;width:30px;height:30px;border-radius:50%;background:var(--blue);color:#fff;font-weight:700;font-size:15px;line-height:30px}
.step b{display:block;margin-top:14px;font-size:17px;color:var(--blue);text-transform:uppercase}
.step small{font-size:12px;text-transform:uppercase;color:var(--ink);line-height:1.3;display:block;margin-top:4px}
.step-arrow{position:absolute;top:220px}

/* lenders */
.lenders{top:1787px;height:206px;background:var(--grey-mid);text-align:center}
.lenders h3{margin-top:40px;font-size:16px;font-weight:700;color:var(--navy);text-transform:uppercase}
.lender-row{position:absolute;left:73px;top:104px;width:1054px;display:flex;align-items:center;justify-content:space-between}
.lender-row .name{width:230px;font-size:34px;font-weight:800;color:#3c3c3c}

/* loan cards */
.loans{top:1993px;height:431px}
.loan-card{position:absolute;top:121px;width:250px;height:275px;background:var(--blue);border-radius:6px;text-align:center;color:#fff;padding-top:84px}
.loan-card .art{position:absolute;left:60px;top:-78px;width:130px;height:130px;border-radius:50%;border:4px solid var(--navy);background:radial-gradient(circle,#ffffff 45%,#d8ecf6 100%)}
.loan-card h4{font-size:18px;font-weight:400}
.loan-card strong{display:block;font-size:40px;font-weight:700;line-height:1.2}
.loan-card small{font-size:10px;text-transform:uppercase}
.loan-card .btn{margin-top:14px;width:105px;height:44px;background:var(--navy);font-size:14px;text-transform:none}

/* reviews */
.reviews{top:2424px;height:303px;text-align:center}
.reviews h2{margin-top:24px}
.review{position:absolute;top:102px;width:286px;height:150px;border:1px solid var(--line);text-align:left;padding:14px 18px}
.review .top{display:flex;justify-content:space-between;font-size:11px}
.stars{color:var(--orange);letter-spacing:2px;font-size:15px}
.review p{font-size:14px;line-height:1.45;margin-top:10px;color:#444}
.review .who{display:flex;align-items:center;gap:8px;margin-top:6px;font-size:13px;font-weight:600;color:var(--blue)}
.avatar{width:32px;height:32px;border-radius:50%;background:#c9cdd0}
.slide-arrow{position:absolute;top:165px}
.rated{position:absolute;left:0;width:1200px;top:266px;font-size:10px;line-height:1.5;color:#888}

/* property */
.property{top:2727px;height:381px;background:var(--grey)}
.property h3{position:absolute;left:73px;top:48px;font-size:21px;color:var(--navy);font-weight:700}
.property p{position:absolute;left:73px;top:84px;font-size:15px}
.property .field{position:absolute;top:211px;height:44px;background:#fff}
.property .btn{position:absolute;left:73px;top:284px;width:383px;height:48px;background:var(--navy);font-size:14px}
.property-art{position:absolute;left:776px;top:40px;width:340px;height:341px;background:linear-gradient(180deg,#eef2f4 0%,#cfe6f2 60%,#b9dcee 100%)}

/* pre approvals */
.preapproval{top:3108px;height:213px;background:var(--blue);text-align:center;color:#fff}
.preapproval h2{margin-top:34px;font-size:29px;font-weight:700;text-transform:uppercase}
.preapproval p{font-size:19px;margin-top:8px}
.preapproval .actions{display:flex;justify-content:center;gap:18px;margin-top:22px}
.preapproval .btn{height:46px;background:var(--navy);font-size:15px;padding:0 32px}

/* footer */
.site-footer{top:3321px;height:242px;background:var(--navy-dark);color:#fff}
.foot-brand{position:absolute;left:73px;top:50px;font-size:24px;font-weight:800;line-height:1.05}
.foot-brand small{display:block;font-size:13px;letter-spacing:3px}
.foot-about{position:absolute;left:73px;top:112px;width:250px;font-size:14px;line-height:1.5;color:#d6e1e8}
.foot-col{position:absolute;top:50px}
.foot-col h5{font-size:13px;font-weight:700;color:var(--blue);text-transform:uppercase;margin-bottom:8px}
.foot-col li{list-style:none;font-size:14px;line-height:32px;color:#e6edf2;white-space:nowrap}
.copyright{top:3563px;height:73px;background:#082537;color:#c9d5dc;font-size:12px}
.copyright span{position:absolute;left:73px;top:28px}
.socials{position:absolute;right:73px;top:26px;display:flex;gap:18px}
.socials i{width:20px;height:20px;border-radius:50%;background:#c9d5dc;display:block}
</style>
</head>
<body>

<header class="section site-header">
  <div class="brand">KELBROOK<small>LENDING SOLUTIONS</small></div>
  <div class="service">
    <svg width="44" height="44" viewBox="0 0 44 44" aria-hidden="true"><circle cx="22" cy="22" r="20" fill="none" stroke="#1c9fd2" stroke-width="2.5"/><path d="M15 12c2-1 4 3 5 5s-2 3-1 5 3 4 5 5 3-2 5-1 5 3 5 5-3 4-5 4c-8-1-15-8-16-16 0-3 1-6 2-7z" fill="#1c9fd2"/></svg>
    <div class="service-text"><span>24/7 Customer Service</span><strong>1300 555 018</strong></div>
  </div>
</header>

<nav class="section main-nav">
  <a href="#"><svg width="16" height="12" viewBox="0 0 16 12" aria-hidden="true"><path d="M2 6l2-4h8l2 4v5H2z" fill="#fff"/></svg>CAR LOANS</a>
  <a href="#"><svg width="14" height="12" viewBox="0 0 14 12" aria-hidden="true"><path d="M7 0l7 6h-2v6H2V6H0z" fill="#fff"/></svg>HOME LOANS</a>
  <a href="#"><svg width="14" height="12" viewBox="0 0 14 12" aria-hidden="true"><rect x="1" y="3" width="12" height="9" fill="#fff"/><rect x="5" y="0" width="4" height="3" fill="#fff"/></svg>COMMERCIAL LOANS</a>
  <a href="#"><svg width="12" height="12" viewBox="0 0 12 12" aria-hidden="true"><circle cx="6" cy="3" r="3" fill="#fff"/><path d="M0 12c0-4 3-5 6-5s6 1 6 5z" fill="#fff"/></svg>PERSONAL LOANS</a>
  <a href="#" class="cta">GET PRE APPROVED</a>
</nav>

<section class="section hero">
  <div class="hero-photo" role="img" aria-label="Photo of a white sedan driving along a coastal road under a cloudy sky"></div>
  <div class="hero-copy">
    <h1>Your Finance.<br>Our Low Rates,<br>In Record Time</h1>
    <a href="#" class="btn">Get A Quick Quote</a>
  </div>
  <form class="quote-box">
    <h3>GET A QUICK QUOTE</h3>
    <div class="hint">Select a loan type from the icons below</div>
    <div class="loan-icons" aria-hidden="true">
      <svg width="22" height="16" viewBox="0 0 22 16"><path d="M2 8l3-6h12l3 6v6H2z" fill="#113f5f"/><circle cx="6" cy="14" r="2" fill="#fff"/><circle cx="16" cy="14" r="2" fill="#fff"/></svg>
      <svg width="22" height="16" viewBox="0 0 22 16"><circle cx="5" cy="11" r="4" fill="none" stroke="#113f5f" stroke-width="2"/><circle cx="17" cy="11" r="4" fill="none" stroke="#113f5f" stroke-width="2"/><path d="M5 11l5-6h5l2 6" fill="none" stroke="#113f5f" stroke-width="2"/></svg>
      <svg width="20" height="16" viewBox="0 0 20 16"><path d="M10 0l10 8h-3v8H3V8H0z" fill="#113f5f"/></svg>
      <svg width="20" height="16" viewBox="0 0 20 16"><rect x="1" y="4" width="18" height="12" fill="#113f5f"/><rect x="7" y="0" width="6" height="4" fill="none" stroke="#113f5f" stroke-width="2"/></svg>
    </div>
    <div class="fields">
      <div class="field">First Name</div><div class="field">Last Name</div>
      <div class="field wide">Email Address</div>
      <div class="field">Phone No</div><div class="field">Postal Code</div>
    </div>
    <div class="business">Finance For Business Purposes <label><i class="radio"></i>No</label><label><i class="radio"></i>Yes</label></div>
    <a href="#" class="btn">Get My Quote</a>
    <p class="terms">By clicking Get My Quote,<br>I acknowledge and accept the Terms &amp; Conditions.</p>
  </form>
</section>

<section class="section rate-strip">
  <div class="best-rate">
    <div class="tag">TODAY'S BEST RATE ON</div>
    <div class="date"><svg width="22" height="22" viewBox="0 0 22 22" aria-hidden="true"><rect x="1" y="3" width="20" height="18" fill="none" stroke="#1f3c52" stroke-width="2"/><rect x="1" y="3" width="20" height="5" fill="#1f3c52"/><rect x="5" y="11" width="3" height="3" fill="#1f3c52"/><rect x="10" y="11" width="3" height="3" fill="#1f3c52"/><rect x="15" y="11" width="3" height="3" fill="#1f3c52"/></svg>MON, MAR 06 2017</div>
  </div>
  <div class="rate-card" style="left:473px"><span>Home loans from</span><strong>3.94<sup>%</sup></strong><em>Variable</em></div>
  <div class="rate-card" style="left:819px"><span>With a low</span><strong>2.54<sup>%</sup></strong><em>Comparison</em></div>
</section>

<section class="section rates-about">
  <div class="interest">
    <h2 class="title">Interest Rates</h2>
    <div class="col-heads"><span>Our<br>Loan rates</span><span>Comparison<br>Rate</span></div>
    <div class="rate-row first"><i class="icon"><svg width="28" height="20" viewBox="0 0 28 20" aria-hidden="true"><path d="M2 10l4-8h16l4 8v8H2z" fill="#fff"/><circle cx="8" cy="17" r="2.5" fill="#1c9fd2"/><circle cx="20" cy="17" r="2.5" fill="#1c9fd2"/></svg></i><span class="name">Car Loan</span><span class="num">4.2%</span><span class="num">5.4%</span><a href="#" class="btn">Apply</a></div>
    <div class="rate-row"><i class="icon"><svg width="30" height="20" viewBox="0 0 30 20" aria-hidden="true"><circle cx="7" cy="13" r="5" fill="none" stroke="#fff" stroke-width="2.5"/><circle cx="23" cy="13" r="5" fill="none" stroke="#fff" stroke-width="2.5"/><path d="M7 13l6-8h6l4 8" fill="none" stroke="#fff" stroke-width="2.5"/></svg></i><span class="name">Bike Loan</span><span class="num">6.69%</span><span class="num">7.4%</span><a href="#" class="btn">Apply</a></div>
    <div class="rate-row"><i class="icon"><svg width="26" height="22" viewBox="0 0 26 22" aria-hidden="true"><path d="M13 0l13 11h-4v11H4V11H0z" fill="#fff"/></svg></i><span class="name">Home Loan</span><span class="num">3.89%</span><span class="num">4.4%</span><a href="#" class="btn">Apply</a></div>
    <div class="rate-row"><i class="icon"><svg width="26" height="22" viewBox="0 0 26 22" aria-hidden="true"><rect x="1" y="6" width="24" height="16" fill="#fff"/><rect x="9" y="1" width="8" height="5" fill="none" stroke="#fff" stroke-width="2.5"/></svg></i><span class="name">Business Loan</span><span class="num">4.2%</span><span class="num">5.4%</span><a href="#" class="btn">Apply</a></div>
  </div>
  <div class="divider"></div>
  <div class="about">
    <h2 class="title">About Our Company</h2>
    <p>Fusce ultricies orci ac feugiat suscipit leo massa sodales velit et scelerisque mi tortor at ipsum cligula augue bibendum accumsan vestibulum ut commodo a mi Morbi ornare</p>
    <p>gravida elit Integer congue augue et malesuada iaculis ipsum dui aliquet felis at cursus magna nisi nec elit Praesent elementum elit at tellus nec ultricies sit amet porttitor mattis enim</p>
    <div class="calc-row">
      <a href="#" class="btn home">Calculate your Home<br>loan repayments<svg width="34" height="30" viewBox="0 0 26 22" aria-hidden="true"><path d="M13 0l13 11h-4v11H4V11H0z" fill="#fff"/></svg></a>
      <a href="#" class="btn car">Calculate your Car<br>Loan repayments<svg width="36" height="26" viewBox="0 0 28 20" aria-hidden="true"><path d="M2 10l4-8h16l4 8v8H2z" fill="#fff"/><circle cx="8" cy="17" r="2.5" fill="#1c9fd2"/><circle cx="20" cy="17" r="2.5" fill="#1c9fd2"/></svg></a>
    </div>
  </div>
</section>

<section class="section how">
  <h2 class="title">How It Works</h2>
  <div class="steps">
    <div class="step"><span class="n">1</span><div class="circle"><svg width="40" height="34" viewBox="0 0 40 34" aria-hidden="true"><rect x="4" y="4" width="32" height="20" rx="2" fill="none" stroke="#113f5f" stroke-width="2.5"/><path d="M0 28h40" stroke="#113f5f" stroke-width="3"/></svg></div><b>Apply</b><small>Online now</small></div>
    <div class="step"><span class="n">2</span><div class="circle"><svg width="34" height="38" viewBox="0 0 34 38" aria-hidden="true"><rect x="4" y="2" width="26" height="34" rx="2" fill="none" stroke="#113f5f" stroke-width="2.5"/><path d="M10 20l5 5 10-11" fill="none" stroke="#1c9fd2" stroke-width="3"/></svg></div><b>Approved</b><small>Instantly</small></div>
    <div class="step"><span class="n">3</span><div class="circle"><svg width="40" height="30" viewBox="0 0 28 20" aria-hidden="true"><path d="M2 10l4-8h16l4 8v8H2z" fill="none" stroke="#113f5f" stroke-width="2"/><circle cx="8" cy="15" r="2" fill="#113f5f"/><circle cx="20" cy="15" r="2" fill="#113f5f"/></svg></div><b>Find</b><small>Locate a vehicle</small></div>
    <div class="step"><span class="n">4</span><div class="circle"><svg width="38" height="38" viewBox="0 0 38 38" aria-hidden="true"><circle cx="19" cy="19" r="15" fill="none" stroke="#113f5f" stroke-width="2.5"/><text x="19" y="26" text-anchor="middle" font-size="20" font-weight="700" fill="#1c9fd2" font-family="Open Sans, sans-serif">$</text></svg></div><b>Funded</b><small>Today or deposited<br>overnight</small></div>
  </div>
  <svg class="step-arrow" style="left:295px" width="54" height="20" viewBox="0 0 54 20" aria-hidden="true"><path d="M2 10h38" stroke="#1c9fd2" stroke-width="3" stroke-dasharray="3 4"/><path d="M40 2l12 8-12 8z" fill="#1c9fd2"/></svg>
  <svg class="step-arrow" style="left:573px" width="54" height="20" viewBox="0 0 54 20" aria-hidden="true"><path d="M2 10h38" stroke="#1c9fd2" stroke-width="3" stroke-dasharray="3 4"/><path d="M40 2l12 8-12 8z" fill="#1c9fd2"/></svg>
  <svg class="step-arrow" style="left:852px" width="54" height="20" viewBox="0 0 54 20" aria-hidden="true"><path d="M2 10h38" stroke="#1c9fd2" stroke-width="3" stroke-dasharray="3 4"/><path d="M40 2l12 8-12 8z" fill="#1c9fd2"/></svg>
</section>

<section class="section lenders">
  <h3>With plenty of lenders to choose from, let us find you the perfect finance solution</h3>
  <div class="lender-row">
    <svg width="14" height="24" viewBox="0 0 14 24" aria-hidden="true"><path d="M12 2L2 12l10 10" fill="none" stroke="#888" stroke-width="3"/></svg>
    <span class="name">Nordway</span>
    <span class="name">HARLEN</span>
    <span class="name" style="font-size:18px">CORBEL FINANCE</span>
    <span class="name">Bluegate</span>
    <svg width="14" height="24" viewBox="0 0 14 24" aria-hidden="true"><path d="M2 2l10 10L2 22" fill="none" stroke="#888" stroke-width="3"/></svg>
  </div>
</section>

<section class="section loans">
  <div class="loan-card" style="left:73px"><div class="art" role="img" aria-label="Illustration of a person standing beside a car"></div><h4>Car Loans – From</h4><strong>4.20 %</strong><small>5.67% comparison rate</small><br><a href="#" class="btn">Apply Now</a></div>
  <div class="loan-card" style="left:341px"><div class="art" role="img" aria-label="Illustration of a family in front of a house"></div><h4>Home Loans – From</h4><strong>3.89 %</strong><small>3.99% comparison rate</small><br><a href="#" class="btn">Apply Now</a></div>
  <div class="loan-card" style="left:609px"><div class="art" role="img" aria-label="Illustration of a rider with a motorbike"></div><h4>Bike Loans – From</h4><strong>6.69 %</strong><small>7.49% comparison rate</small><br><a href="#" class="btn">Apply Now</a></div>
  <div class="loan-card" style="left:877px"><div class="art" role="img" aria-label="Illustration of a tradesperson with a work van"></div><h4>Business Loans – From</h4><strong>4.20 %</strong><small>4.99% comparison rate</small><br><a href="#" class="btn">Apply Now</a></div>
</section>

<section class="section reviews">
  <h2 class="title">Customer Reviews</h2>
  <svg class="slide-arrow" style="left:75px" width="14" height="24" viewBox="0 0 14 24" aria-hidden="true"><path d="M12 2L2 12l10 10" fill="none" stroke="#888" stroke-width="3"/></svg>
  <div class="review" style="left:150px"><div class="top"><span class="stars">★★★★★</span><span>6 days ago</span></div><p>Vestibulum ante ipsum primis in faucibus orci luctus et ultrices posuere cubilia</p><div class="who">Maya Cortell<i class="avatar"></i></div></div>
  <div class="review" style="left:460px"><div class="top"><span class="stars">★★★★★</span><span>6 days ago</span></div><p>Vestibulum ante ipsum primis in faucibus orci luctus et ultrices posuere cubilia</p><div class="who">Maya Cortell<i class="avatar"></i></div></div>
  <div class="review" style="left:771px"><div class="top"><span class="stars">★★★★★</span><span>6 days ago</span></div><p>Vestibulum ante ipsum primis in faucibus orci luctus et ultrices posuere cubilia</p><div class="who">Maya Cortell<i class="avatar"></i></div></div>
  <svg class="slide-arrow" style="left:1110px" width="14" height="24" viewBox="0 0 14 24" aria-hidden="true"><path d="M2 2l10 10L2 22" fill="none" stroke="#888" stroke-width="3"/></svg>
  <p class="rated">Rated <b>9.3</b> out of 10 based on <b>495</b> reviews. See some of the reviews here.<br>Powered by Quill Gauge</p>
</section>

<section class="section property">
  <h3>BUYING PROPERTY OR LOOKING TO REFINANCE?</h3>
  <p>Find out what it's worth today with our free home property report!</p>
  <div class="field" style="left:73px;width:303px">Name</div>
  <div class="field" style="left:405px;width:288px">E-mail</div>
  <a href="#" class="btn">Email me my free property report</a>
  <div class="property-art" role="img" aria-label="Illustration of a family standing in front of their house"></div>
</section>

<section class="section preapproval">
  <h2>Express Pre Approvals</h2>
  <p>In A Hurry ? Call Us On 1300 555 018 For Even Pre Approvals</p>
  <div class="actions"><a href="#" class="btn">Apply Now</a><a href="#" class="btn">Get A Quote</a></div>
</section>

<footer class="section site-footer">
  <div class="foot-brand">KELBROOK<small>LENDING SOLUTIONS</small></div>
  <p class="foot-about">Kelbrook Lending Solutions is a trading name of Northside Car Loans Pty Ltd</p>
  <div class="foot-col" style="left:388px"><h5>Site Map</h5><ul><li>Car Loans</li><li>Personal Loans</li><li>Home Loans</li><li>Commercial Loans</li></ul></div>
  <div class="foot-col" style="left:606px"><h5>Extra Links</h5><ul><li>Privacy</li><li>Terms &amp; Conditions</li><li>Credit Guide &amp; Quote</li><li>Investor relations</li></ul></div>
  <div class="foot-col" style="left:848px"><h5>Open Hours</h5><ul><li>Monday 8am-7pm</li><li>Tuesday-Friday 8am-6pm</li><li>Saturday 10am-2pm</li><li>Sunday CLOSED</li><li>Level 2, 38 Pittwater Road Dee Why NSW 2099</li></ul></div>
</footer>

<div class="section copyright">
  <span>Copyright © 2017. Company Name. All Right Reserved</span>
  <div class="socials" aria-hidden="true"><i></i><i></i><i></i><i></i><i></i><i></i></div>
</div>

</body>
</html>
```